Massage Therapy and Energy Healing Practice

I am a massage therapist, Reiki energy healer, I sell herbs and oils, and also a health lifestyle coach. I need a design that is strong because I'm not a spa. I do therapeutic work, but I want a touch of the energy and spiritual healing I do as well to be included in the design. I like blue, green, or purple colors. I live in the Blue Ridge Mountains of VA and even though my practice is in the city I like my love for nature and the earth to show through. I would like a single image logo so I can use the image many places. I need a strong brand that will let others know that I combine massage therapy in a therapeutic way while keeping my touches of energy healing, nurturing, herb crafting, and mother earth loving ways.
Updates

Just some things about me:I like to hike. I live on a farm. I own horses, cows, sheep and dogs. I love nature and the energy in produces. I'm very spiritual. I don't know how these things might help or if they do, but I know that my personality might help inspire what I will find good in a design. Added Sunday, December 13, 2015

Target Market(s)

People in pain. People who need spiritual council. Need herbal medicine advice. Holistic healthcare.

Industry/Entity Type

Massage

Contact Information for Business Card

Kneadwell Studio
Lorna T. Whitcombe C.M.T, R.M.T
40519 Hollin Creek Court, Tallowdale, VA
540-718-2437

Colors
3176b5
85abd2
876aae
9bcb3c

Requirements
Must have
• Strong Branding that promotes my massage therapy practice first
Nice to have
• Something to evoke my herbal medicine, my energy healing, my spiritual side

```html
<!DOCTYPE html>
<html lang="en">
<head>
<meta charset="utf-8">
<title>Kneadwell Studio — Business Card</title>
<link rel="stylesheet" href="https://fonts.googleapis.com/css2?family=Questrial&display=swap">
<style>
  :root {
    --brand-blue: #3176b5;
    --brand-blue-light: #4a8fd0;
    --brand-green: #9bcb3c;
    --brand-green-light: #a9d44a;
    --ink-grey: #8a8a8a;
    --card-white: #ffffff;
    --stage: #e9e6e1;
  }
  * { box-sizing: border-box; margin: 0; padding: 0; }
  html, body {
    width: 1200px;
    height: 900px;
    overflow: hidden;
    background: var(--stage);
    font-family: "Questrial", "Century Gothic", sans-serif;
  }
  .stage {
    position: relative;
    width: 1200px;
    height: 900px;
  }
  .card {
    position: absolute;
    left: 340px;
    width: 520px;
    height: 297px;
    border-radius: 18px;
    overflow: hidden;
    box-shadow: 0 6px 18px rgba(0, 0, 0, 0.18);
  }
  /* Front */
  .card--front {
    top: 110px;
    background: linear-gradient(135deg, var(--brand-blue-light), var(--brand-blue));
  }
  .card--front .split-green {
    position: absolute;
    inset: 0;
    background: linear-gradient(135deg, var(--brand-green-light), var(--brand-green));
    clip-path: polygon(0 0, 54% 0, 44% 100%, 0 100%);
  }
  .card--front .brand-name {
    position: absolute;
    left: 0;
    right: 0;
    top: 50%;
    transform: translateY(-50%);
    text-align: center;
    color: var(--card-white);
    font-size: 40px;
    letter-spacing: 0.5px;
  }
  /* Back */
  .card--back {
    top: 490px;
    background: var(--card-white);
  }
  .card--back .brand-name {
    position: absolute;
    left: 0;
    right: 0;
    top: 44px;
    text-align: center;
    color: var(--brand-blue);
    font-size: 30px;
  }
  .contact {
    position: absolute;
    left: 70px;
    top: 112px;
    color: var(--ink-grey);
  }
  .contact__name {
    font-size: 27px;
    line-height: 1.1;
  }
  .contact__credentials {
    color: var(--brand-green);
    font-size: 16px;
    letter-spacing: 1px;
    margin: 4px 0 10px;
  }
  .contact__row {
    display: flex;
    align-items: flex-start;
    gap: 12px;
    font-size: 16px;
    line-height: 1.45;
    margin-bottom: 6px;
  }
  .contact__icon {
    width: 18px;
    height: 18px;
    flex: 0 0 18px;
    margin-top: 3px;
    fill: var(--brand-blue);
  }
</style>
</head>
<body>
  <main class="stage">
    <section class="card card--front" aria-label="Card front">
      <div class="split-green"></div>
      <p class="brand-name">Kneadwell Studio</p>
    </section>

    <section class="card card--back" aria-label="Card back">
      <p class="brand-name">Kneadwell Studio</p>
      <div class="contact">
        <p class="contact__name">Lorna T. Whitcombe</p>
        <p class="contact__credentials">C.M.T, R.M.T</p>
        <div class="contact__row">
          <svg class="contact__icon" viewBox="0 0 24 24" aria-hidden="true">
            <path d="M12 2a7 7 0 0 0-7 7c0 5.2 7 13 7 13s7-7.8 7-13a7 7 0 0 0-7-7zm0 9.5A2.5 2.5 0 1 1 12 6.5a2.5 2.5 0 0 1 0 5z"/>
          </svg>
          <address style="font-style:normal">40519 Hollin Creek Court<br>Tallowdale, VA</address>
        </div>
        <div class="contact__row">
          <svg class="contact__icon" viewBox="0 0 24 24" aria-hidden="true">
            <path d="M2 9c0-2 4-4 10-4s10 2 10 4v2h-5V9.5c-1.5-.5-3-.7-5-.7s-3.5.2-5 .7V11H2z"/>
            <path d="M6 12l2-2h8l2 2 2 7H4zm6 1.5a2.5 2.5 0 1 0 0 5 2.5 2.5 0 0 0 0-5z"/>
          </svg>
          <span>540-718-2437</span>
        </div>
      </div>
    </section>
  </main>
</body>
</html>
```